依頼概要
■依頼の目的/概要
小学生バレーボールのスポーツ少年団でメンバーを募集するためのポスターの作成をお願いします。

■依頼詳細
ポスターは男子チーム、女子チーム兼用となります。主に教室での直接配布、校内の掲示板や近隣の施設(コンビニや公民館等)での掲示を目的としたものになります。

必要に応じて写真の背景等を加工いただいても構いません。

楽しそうなイメージだけでなく、スポーツに関心のある子どもたちがバレーボールを“かっこいい”と感じてくれるような躍動感の伝わるものを希望しています。

■重視する点
・明るくインパクトのあるデザイン
・できるだけ躍動感の伝わるもの
・読みやすい文字であること

■サイズ
A4サイズでお願いします。
メインはA4ですが、B4(A4の122%)にも対応する画素数でお願いいたします

■その他
・レイアウトイメージ、素材は添付ファイルにてご確認ください
・写真やイラストの素材は当方で用意していますが、用意したもの以外の素材を使っていただいても構いません。
・レイアウトのイメージやキャッチコピー、掲載する文言等は添付の「レイアウトイメージ.pdf」「レイアウト説明.txt」を参照ください。レイアウトは当方のイメージと異なるものになっても構いません。

何かご不明な点がございましたら、お気軽にご質問下さい。
どうぞよろしくお願いいたします。
納品いただくデータですが、納品後に当方で編集することがあるため、フォトショップまたはイラストレーターで編集できるかたちで納品いただけますと幸いです。よろしくお願いします。

```html
<!DOCTYPE html>
<html lang="ja">
<head>
<meta charset="utf-8">
<title>若葉バレー スポーツ少年団 新メンバー募集</title>
<link href="https://fonts.googleapis.com/css2?family=Dela+Gothic+One&family=Noto+Sans+JP:wght@400;700;900&display=swap" rel="stylesheet">
<style>
  :root{
    --ink:#161616;
    --ink-soft:#2a2a2a;
    --red:#e2232a;
    --red-deep:#a8141a;
    --yellow:#ffe200;
    --white:#ffffff;
    --blue:#1f5fd1;
    --photo-a:#6b6660;
    --photo-b:#3d3a38;
    --skin:#e9b894;
  }
  *{margin:0;padding:0;box-sizing:border-box}
  html,body{width:849px;height:1200px;overflow:hidden;background:var(--ink)}
  body{font-family:"Noto Sans JP",sans-serif;color:var(--white)}
  .poster{position:relative;width:849px;height:1200px;overflow:hidden;background:var(--ink)}
  .backdrop{position:absolute;inset:0}

  .headline{position:absolute;z-index:3;left:36px;top:14px;font-family:"Dela Gothic One",sans-serif;line-height:1;letter-spacing:2px}
  .headline__lead{display:block;font-size:78px;color:var(--white)}
  .headline__sport{display:block;margin:14px 0 0 30px;font-size:84px;color:var(--yellow);-webkit-text-stroke:3px var(--ink);paint-order:stroke fill;text-shadow:5px 5px 0 var(--red)}
  .headline__tail{display:block;margin:12px 0 0 300px;font-size:80px;color:var(--white);text-shadow:5px 5px 0 var(--red)}

  .art{position:absolute}
  .art--hero{z-index:1;right:0;top:0;width:210px;height:230px;background:linear-gradient(160deg,#f4f4f4 0%,#d9d9d9 55%,var(--red) 100%);clip-path:polygon(22% 0,100% 0,100% 100%,0 80%)}
  .art--kid-right{right:10px;top:610px;width:160px;height:190px;background:linear-gradient(180deg,var(--skin),var(--red));border-radius:40% 40% 20% 20%}
  .art--kid-mid{left:300px;top:1000px;width:100px;height:140px;background:linear-gradient(180deg,var(--skin),var(--red));border-radius:45% 45% 20% 20%}
  .art--kid-corner{right:10px;top:1025px;width:110px;height:165px;background:linear-gradient(180deg,var(--skin),var(--red));border-radius:45% 45% 20% 20%}

  .photo{position:absolute;background:linear-gradient(135deg,var(--photo-a),var(--photo-b));border:5px solid var(--white);box-shadow:0 6px 0 rgba(0,0,0,.45)}
  .photo--reception{left:14px;top:300px;width:380px;height:175px;transform:rotate(-3deg)}
  .photo--warmup{left:400px;top:285px;width:430px;height:165px;transform:rotate(2deg)}
  .photo--team{left:100px;top:448px;width:560px;height:140px;transform:rotate(-1deg)}

  .bubble{position:absolute;z-index:2;background:var(--white);color:var(--ink);font-weight:900;font-size:17px;line-height:1.3;padding:8px 16px;border-radius:22px;border:3px solid var(--red);text-align:center}
  .bubble--spike{left:46px;top:262px;transform:rotate(-4deg)}
  .bubble--butterfly{left:632px;top:372px;transform:rotate(4deg)}
  .bubble--indoor{left:590px;top:478px;transform:rotate(-3deg)}
  .bubble--safety{left:26px;top:536px;transform:rotate(-6deg)}

  .title{position:absolute;left:34px;top:606px}
  .title__team{display:flex;align-items:center;gap:14px}
  .title__name{font-family:"Dela Gothic One",sans-serif;font-size:82px;line-height:1;color:var(--white);text-shadow:5px 5px 0 var(--red)}
  .title__org{font-family:"Dela Gothic One",sans-serif;font-size:34px;line-height:1.15;color:var(--white)}
  .title__recruit{display:flex;align-items:center;gap:6px;margin-top:18px}
  .sex{display:inline-block;width:62px;height:62px;line-height:62px;text-align:center;font-family:"Dela Gothic One",sans-serif;font-size:44px;color:var(--white)}
  .sex--boy{background:var(--blue)}
  .sex--girl{background:var(--red)}
  .title__call{margin-left:10px;font-family:"Dela Gothic One",sans-serif;font-size:62px;line-height:1;color:var(--yellow);-webkit-text-stroke:2px var(--ink);paint-order:stroke fill}

  .intro{position:absolute;left:40px;top:800px;width:640px;font-size:14px;font-weight:700;line-height:1.6}

  .schedule{position:absolute;left:28px;top:862px;width:262px;height:314px;background:var(--white);color:var(--ink);padding:18px 18px;border-top:8px solid var(--red)}
  .schedule__label{font-weight:900;font-size:20px;margin-bottom:12px}
  .schedule__time{font-family:"Dela Gothic One",sans-serif;font-size:27px;line-height:1.15}
  .schedule__place{font-size:13px;font-weight:700;line-height:1.5;margin:6px 0 20px}

  .visit{position:absolute;left:410px;top:866px;width:340px;background:var(--red);padding:14px 16px;font-family:"Dela Gothic One",sans-serif;font-size:22px;line-height:1.3;color:var(--white);white-space:nowrap}
  .visit__note{display:block;margin-top:6px;font-family:"Noto Sans JP",sans-serif;font-weight:700;font-size:12px}

  .info{position:absolute;left:410px;top:1010px;width:300px}
  .info__row{display:flex;align-items:flex-start;gap:10px;margin-bottom:10px;font-size:13px;font-weight:700;line-height:1.5}
  .info__key{flex:none;background:var(--yellow);color:var(--ink);font-weight:900;font-size:12px;padding:1px 6px}
  .info__tel{display:flex;align-items:center;gap:8px;font-family:"Dela Gothic One",sans-serif;font-size:22px;color:var(--yellow);white-space:nowrap}
</style>
</head>
<body>
<main class="poster">
  <svg class="backdrop" width="849" height="1200" viewBox="0 0 849 1200" aria-hidden="true">
    <polygon points="0,250 849,210 849,610 0,650" fill="var(--ink-soft)"/>
    <polygon points="0,280 260,260 140,620 0,630" fill="var(--red-deep)"/>
    <polygon points="560,250 849,230 849,560 700,600" fill="var(--red)"/>
    <polygon points="0,600 849,560 849,590 0,632" fill="var(--red)"/>
    <polygon points="0,840 849,820 849,832 0,852" fill="var(--red)"/>
  </svg>

  <div class="art art--hero" role="img" aria-label="スパイクを打つ女の子のイラスト"></div>

  <h1 class="headline">
    <span class="headline__lead">そうだ、</span>
    <span class="headline__sport">バレーボール</span>
    <span class="headline__tail">しよう。</span>
  </h1>

  <div class="photo photo--reception" role="img" aria-label="体育館でレシーブ練習をする子どもたちの写真"></div>
  <div class="photo photo--warmup" role="img" aria-label="体育館で整列して準備運動をする子どもたちの写真"></div>
  <div class="photo photo--team" role="img" aria-label="おそろいのTシャツで並ぶチームの後ろ姿の写真"></div>

  <p class="bubble bubble--spike">レシーブ!スパイク!<br>キマると気持ちいい!</p>
  <p class="bubble bubble--butterfly">チョウのように舞い!<br>ハチのように!?</p>
  <p class="bubble bubble--indoor">屋内だから夏場も<br>雨の日も安心!</p>
  <p class="bubble bubble--safety">感染症対策も<br>しています!</p>

  <section class="title">
    <div class="title__team">
      <span class="title__name">若葉バレー</span>
      <span class="title__org">スポーツ<br>少年団</span>
    </div>
    <div class="title__recruit">
      <span class="sex sex--boy">男</span><span class="sex sex--girl">女</span>
      <span class="title__call">新メンバー募集!!</span>
    </div>
  </section>

  <div class="art art--kid-right" role="img" aria-label="ボールを持つ子どものイラスト"></div>

  <p class="intro">みんなで声をかけ合いながら楽しく練習しているよ!<br>いろいろな小学校から集まっているから友だちもたくさんできるよ!</p>

  <section class="schedule">
    <p class="schedule__label">【練習日(毎週)】</p>
    <p class="schedule__time">土・日曜日 9:00~</p>
    <p class="schedule__place">若葉小学校体育館・<br>若葉西小学校体育館</p>
    <p class="schedule__time">水曜日 17:30~</p>
    <p class="schedule__place">若葉小学校体育館</p>
  </section>

  <div class="art art--kid-mid" role="img" aria-label="レシーブする女の子のイラスト"></div>

  <section class="visit">見学・体験は<br>いつでも受け付けています!
    <span class="visit__note">下記の連絡先までお気軽にどうぞ。</span>
  </section>

  <section class="info">
    <div class="info__row"><span class="info__key">持ち物</span><span>上ぐつ、水とう、動きやすい服そう</span></div>
    <div class="info__row"><span class="info__key">連絡先</span><span>若葉バレースポーツ少年団<br>育成会会長 川井(カワイ)まで</span></div>
    <div class="info__tel">
      <svg width="22" height="22" viewBox="0 0 24 24" aria-hidden="true"><path fill="var(--yellow)" d="M6.6 10.8a15.1 15.1 0 0 0 6.6 6.6l2.2-2.2c.3-.3.7-.4 1-.2 1.1.4 2.300.6 3.600.6.6 0 1 .4 1 1V20c0 .6-.4 1-1 1A17 17 0 0 1 3 4c0-.6.4-1 1-1h3.5c.6 0 1 .4 1 1 0 1.3.2 2.5.6 3.6.1.3 0 .7-.2 1z"/></svg>
      090-XXXX-XXXX
    </div>
  </section>

  <div class="art art--kid-corner" role="img" aria-label="ガッツポーズをする男の子のイラスト"></div>
</main>
</body>
</html>
```